2367 Halvorsen Avenue Medical Centre

We are looking for a design for new medical clinic.
We are accepting new patients at this new medical centre grand opening. Walk-ins are welcome.
Our cardiac and vascular surgical specialists are department heads at St Alder's Hospital, a leading teaching hospital in Toronto. These specialists will see cardiovascular consults are well as pre-surgical and post-surgical consultations and follow-ups.
Our lab is affiliated with several nuclear medicine clinics in the GTA.
Our Services Includes:
Family Practice
Cardiology Diagnostics
Cardiac & Vascular Surgical Consultation
Ultrasound & Vascular Testing
Open 6 days a week.
Ample Free Parking
Friendly Staffs

Target Market(s)

New Patients. Families of any age. Ethnic groups including Asians & Africans.

Industry/Entity Type

Medical

Font styles to use
Serif
Sans Serif
Decorative
Script
Other font styles liked:
• Arial calibri, verdana

Requirements
Must have
• Address:
• 2367 Halvorsen Avenue East
• Unit 225
• Scarborough, Ontario
• K7T 2P4
• Tel: (416) 555-0148
Nice to have
• Caring and inviting environment.
• Simple but classy.
• Standout colors.
Should not have
• Busy images. Aside from this, any ideas are welcome.

```html
<!DOCTYPE html>
<html lang="en">
<head>
<meta charset="utf-8">
<title>New Medical Clinic Flyer</title>
<link href="https://fonts.googleapis.com/css2?family=Montserrat:wght@500;600;700;800&display=swap" rel="stylesheet">
<style>
  :root {
    --page-bg: #ececec;
    --flyer-top: #e6eff4;
    --flyer-mid: #d7e6ee;
    --brand-blue: #1a7fcf;
    --wave-blue: #3b86c8;
    --wave-light: #bcdced;
    --navy: #2b2f7a;
    --ink: #111111;
    --muted: #6f6f6f;
    --green: #1f8a45;
    --white: #ffffff;
  }
  * { margin: 0; padding: 0; box-sizing: border-box; }
  html, body {
    width: 1200px; height: 1000px; overflow: hidden;
    background: var(--page-bg);
    font-family: "Montserrat", Arial, sans-serif;
  }
  .flyer {
    position: absolute; left: 255px; top: 55px;
    width: 690px; height: 890px; overflow: hidden;
    background: linear-gradient(180deg, var(--flyer-top) 0%, var(--flyer-mid) 100%);
    box-shadow: 0 4px 16px rgba(0,0,0,0.18);
  }
  .backdrop-photo {
    position: absolute; left: 200px; top: 100px; width: 490px; height: 460px;
    background: radial-gradient(ellipse at 60% 50%, #cfdee7 0%, rgba(215,230,238,0) 70%);
  }
  .doctor-photo {
    position: absolute; left: 35px; top: 120px; width: 320px; height: 520px;
    background: linear-gradient(180deg, #dfe7ec 0%, #f4f7f9 40%, #e9eef2 100%);
    border-radius: 140px 140px 0 0;
  }
  .waves { position: absolute; left: 0; top: 0; width: 690px; height: 890px; }
  .title {
    position: absolute; left: 0; right: 0; top: 46px;
    text-align: center; color: var(--brand-blue);
    font-size: 51px; font-weight: 700; letter-spacing: 0.5px;
  }
  .services-label {
    position: absolute; left: 365px; top: 138px; width: 235px; height: 26px;
    background: var(--navy); color: var(--white); border-radius: 4px;
    font-size: 17px; font-weight: 700; text-align: center; line-height: 26px;
    letter-spacing: 0.5px;
  }
  .service {
    position: absolute; left: 305px; width: 360px; text-align: center;
    color: var(--ink); font-size: 18.5px; font-weight: 800; line-height: 23px;
    letter-spacing: 0.4px;
  }
  .service-num {
    display: block; margin: 0 auto 6px; width: 36px; height: 36px; border-radius: 50%;
    background: var(--brand-blue); color: var(--white);
    font-size: 22px; font-weight: 500; line-height: 36px;
  }
  .contact { position: absolute; left: 35px; top: 685px; width: 300px; }
  .contact-lead { color: var(--muted); font-size: 16.5px; font-weight: 500; }
  .contact-phone {
    display: flex; align-items: center; gap: 6px; margin-top: 2px;
    color: var(--ink); font-size: 35px; font-weight: 700; letter-spacing: 0.3px;
  }
  .contact-address {
    margin-top: 4px; padding-left: 55px; font-size: 12px; line-height: 15px; color: var(--ink);
  }
  .badge {
    position: absolute; left: 350px; top: 580px; width: 276px; height: 276px;
    border-radius: 50%; background: var(--green);
    border: 4px solid var(--white); outline: 2px solid var(--green);
    color: var(--white); text-align: center; font-weight: 600;
    display: flex; flex-direction: column; justify-content: center; align-items: center;
  }
  .badge-main { font-size: 28.5px; line-height: 34px; }
  .badge-rule { width: 236px; border-top: 2px dotted var(--white); margin: 14px 0 12px; }
  .badge-sub { font-size: 24px; line-height: 31px; }
</style>
</head>
<body>
  <main class="flyer">
    <div class="backdrop-photo" role="img" aria-label="Soft faded photo of caring hands"></div>
    <div class="doctor-photo" role="img" aria-label="Photo of a smiling senior doctor in a white coat with a stethoscope"></div>

    <svg class="waves" viewBox="0 0 690 890" aria-hidden="true">
      <path d="M0,662 C200,592 450,562 690,560 L690,890 L0,890 Z" fill="#ffffff"/>
      <path d="M0,656 C200,580 450,546 690,543 L690,562 C450,566 200,596 0,664 Z" fill="var(--wave-blue)"/>
      <path d="M0,890 C250,852 450,832 690,828 L690,890 Z" fill="var(--wave-light)"/>
      <path d="M0,888 C250,832 450,806 690,800 L690,815 C450,822 250,846 0,890 Z" fill="var(--wave-blue)"/>
    </svg>

    <h1 class="title">NEW MEDICAL CLINIC</h1>

    <div class="services-label">SERVICES INCLUDES</div>
    <div class="service" style="top:182px"><span class="service-num">1</span>FAMILY PRACTICE</div>
    <div class="service" style="top:262px"><span class="service-num">2</span>CARDIOLOGY DIAGNOSTICS</div>
    <div class="service" style="top:340px"><span class="service-num">3</span>CARDIAC &amp; VASCULAR<br>SURGICAL CONSULTATION</div>
    <div class="service" style="top:445px"><span class="service-num">4</span>ULTRASOUND &amp;<br>VASCULAR</div>

    <section class="contact">
      <p class="contact-lead">To Book Appointment Please Call</p>
      <p class="contact-phone">
        <svg width="30" height="30" viewBox="0 0 30 30" aria-hidden="true">
          <circle cx="15" cy="15" r="13" fill="none" stroke="var(--brand-blue)" stroke-width="2"/>
          <path d="M10 8 l3 0 l1 4 l-2 1.5 a9 9 0 0 0 4.5 4.5 l1.5 -2 l4 1 l0 3 a2 2 0 0 1 -2 2 a13 13 0 0 1 -12 -12 a2 2 0 0 1 2 -2 z" fill="var(--brand-blue)"/>
        </svg>
        (416) 555-0148
      </p>
      <p class="contact-address">2367 Halvorsen Avenue East Unit 225<br>Scarborough, Ontario K7T 2P4</p>
    </section>

    <div class="badge">
      <p class="badge-main">ACCEPTING<br>WALK-IN<br>PATIENTS</p>
      <div class="badge-rule"></div>
      <p class="badge-sub">OPEN 6 DAYS<br>A WEEK.</p>
    </div>
  </main>
</body>
</html>
```